International music label TKPL is looking for CD cover logo design

We are looking for a CD cover for a music CD (online / Tunevale).

- Size: 3000 x 3000 pixels
- Format: JPG

It's about a happy birthday song, which I sing in different styles. There is a volume 1, volume 2, volume 3 to volume 20. (Volume: Jazz, Funk, Rock, Latin, ..) I would like to enter the text for the name of the volume myself in the cover.
Which tool can you recommend to us to enter the text in your design / cover layout yourself?

We look forward to design ideas.

------------------
Text in the cover:
MARELDA
Happy Birthday (plus text with 22 letters - will be entered by myself)

Volume 1 (Text "JAZZ" is entered by myself instead of "Volume 1")
----------------

A birthday should be recognizable in the picture; That means, for example, a balloon (Volume 1 in the balloon), or a gift package or a cake.
Each volume should have a different color (e.g. from a balloon or gift or a colored bar behind the text Volume), but the same design.

The CD cover design should contain Marelda's head / portrait according to the attached jpg. Without hat / please touch the hat away. The head should not be tilted down; please turn upwards so that the head sings in a horizontal direction.
One idea is to frame the head with a colored circle and to add, for example, note symbols in the circle. See attached logo and logotype on www.marelda-example.com. The circle around the head is not a mandatory requirement.

The music direction / volume should be easily recognizable and readable (online e.g. Sonara, Tunevale, Plinko). e.g. Afro Beat, or Oriental or Jazz. ONLY through this term and the color differentiation, the genre of music on the CD cover can be recognized.

Please do not display the TKPL logo on the CD cover.

The layout should address a very broad target group. Music listeners from jazz, rock, reggae, house, dance, classical, African, Indian, Chinese .. also children,

Target Market(s)

worldwide, all ages. On-line. Social media. All musical genres.

Industry/Entity Type

Music Download

Requirements
Must have
• Marelda's head according to the attached jpg must be shown on the CD cover layout. The gaze / sing direction is horizontal (not inclined downwards as in the photo). The hat in the photo must be touched off.
Nice to have
• Colored circle around the head. e.g. with notes in the circle.

```html
<!DOCTYPE html>
<html lang="en">
<head>
<meta charset="utf-8">
<title>Marelda – Happy Birthday – Volume 1</title>
<link href="https://fonts.googleapis.com/css2?family=Playfair+Display:wght@500&family=Great+Vibes&family=Oswald:wght@600&display=swap" rel="stylesheet">
<style>
  :root {
    --cover-red: #ff3441;
    --sun-yellow: #fbb526;
    --photo-light: #f7c75a;
    --photo-dark: #6a2a16;
    --title-cream: #fff4cf;
    --blush: #ffd7da;
    --white: #ffffff;
    --shadow-red: #a3101c;
    --volume-maroon: #4e0e16;
    --balloon-gold: #f3cf6a;
    --balloon-gold-light: #fff0b5;
    --balloon-pearl: #ece9e3;
    --balloon-pearl-light: #ffffff;
  }
  html, body {
    margin: 0;
    padding: 0;
    overflow: hidden;
    background: var(--cover-red);
  }
  .cover {
    position: relative;
    width: 1200px;
    height: 1200px;
    overflow: hidden;
    background: var(--cover-red);
  }
  .artist-name {
    position: absolute;
    top: 18px;
    left: 0;
    width: 1200px;
    margin: 0;
    text-align: center;
    font-family: "Playfair Display", serif;
    font-weight: 500;
    font-size: 136px;
    letter-spacing: 4px;
    color: var(--title-cream);
    line-height: 1;
    padding-left: 14px;
    box-sizing: border-box;
  }
  .portrait-circle {
    position: absolute;
    left: 168px;
    top: 168px;
    width: 864px;
    height: 864px;
    border-radius: 50%;
    background: var(--sun-yellow);
    overflow: hidden;
  }
  .portrait-photo {
    position: absolute;
    inset: 0;
    background: radial-gradient(ellipse 60% 70% at 55% 45%, var(--photo-light) 0%, var(--sun-yellow) 55%, #c77a2a 80%, var(--photo-dark) 100%);
    opacity: 0.85;
  }
  .balloon {
    position: absolute;
  }
  .balloon-gold { left: 28px; top: 96px; }
  .balloon-pearl { left: 994px; top: 144px; }
  .song-title {
    position: absolute;
    left: 0;
    top: 900px;
    width: 1200px;
    margin: 0;
    text-align: center;
    font-family: "Great Vibes", cursive;
    font-weight: 400;
    font-size: 186px;
    line-height: 1.2;
    text-shadow: 3px 4px 0 var(--shadow-red);
    white-space: nowrap;
  }
  .song-title .word-happy { color: var(--blush); }
  .song-title .word-birthday { color: var(--white); margin-left: 24px; }
  .volume-label {
    position: absolute;
    left: 0;
    top: 1128px;
    width: 1200px;
    margin: 0;
    text-align: center;
    font-family: "Oswald", sans-serif;
    font-weight: 600;
    font-size: 40px;
    letter-spacing: 6px;
    color: var(--volume-maroon);
    line-height: 1;
  }
</style>
</head>
<body>
  <main class="cover">
    <svg class="balloon balloon-gold" width="216" height="290" viewBox="0 0 216 290" role="img" aria-label="Gold party balloon">
      <defs>
        <radialGradient id="goldShine" cx="35%" cy="30%" r="70%">
          <stop offset="0%" stop-color="var(--balloon-gold-light)"/>
          <stop offset="100%" stop-color="var(--balloon-gold)"/>
        </radialGradient>
      </defs>
      <ellipse cx="108" cy="136" rx="104" ry="132" fill="url(#goldShine)"/>
      <path d="M100 266 L116 266 L112 278 L104 278 Z" fill="var(--balloon-gold)"/>
    </svg>

    <svg class="balloon balloon-pearl" width="196" height="272" viewBox="0 0 196 272" role="img" aria-label="Pearl white party balloon">
      <defs>
        <radialGradient id="pearlShine" cx="35%" cy="30%" r="70%">
          <stop offset="0%" stop-color="var(--balloon-pearl-light)"/>
          <stop offset="100%" stop-color="var(--balloon-pearl)"/>
        </radialGradient>
      </defs>
      <ellipse cx="98" cy="124" rx="94" ry="122" fill="url(#pearlShine)"/>
      <path d="M90 244 L106 244 L102 256 L94 256 Z" fill="var(--balloon-pearl)"/>
    </svg>

    <h1 class="artist-name">MARELDA</h1>

    <div class="portrait-circle">
      <div class="portrait-photo" role="img" aria-label="Duotone portrait of the singer with gloved hands raised beside her face, singing joyfully"></div>
    </div>

    <h2 class="song-title"><span class="word-happy">Happy</span><span class="word-birthday">Birthday</span></h2>

    <p class="volume-label">VOLUME 1</p>
  </main>
</body>
</html>
```